Valtesh Spinal Care and Performance

We need new business cards, something more modern, clean. On the back of the card maybe a quote. The Dr. likes, “The doctor of the future will give no medicine, but will interest his patient in the care of the human frame, in diet and in the cause and prevention of disease.” - Walter Pimsley. We are open to other suggestions. We are a chiropractic office.

```html
<!DOCTYPE html>
<html lang="en">
<head>
<meta charset="utf-8">
<title>Valtesh Spinal Care and Performance – Business Card</title>
<link rel="stylesheet" href="https://fonts.googleapis.com/css2?family=Source+Sans+3:ital,wght@0,400;0,600;0,700;1,400&display=swap">
<style>
  :root {
    --backdrop: #2b2b2b;
    --card-white: #ffffff;
    --plum: #35123b;
    --plum-text: #6b2a78;
    --lime: #9cba2c;
    --lime-soft: #b9cf44;
    --ink: #2a2a2a;
    --divider: #555555;
  }
  html, body {
    margin: 0;
    width: 1200px;
    height: 1021px;
    overflow: hidden;
    background: var(--backdrop);
    font-family: "Source Sans 3", sans-serif;
  }
  .stage {
    position: relative;
    width: 1200px;
    height: 1021px;
  }
  .card {
    position: absolute;
    left: 330px;
    width: 540px;
    height: 309px;
    box-shadow: 0 10px 24px rgba(0,0,0,0.45);
    overflow: hidden;
  }
  /* back side */
  .card-back {
    top: 171px;
    background: var(--plum);
    display: flex;
    align-items: center;
    justify-content: center;
  }
  .quote {
    width: 400px;
    margin: 0;
    text-align: center;
    color: var(--card-white);
    font-size: 15px;
    line-height: 1.4;
  }
  .quote-intro { display: block; font-style: normal; }
  .quote-body { font-style: italic; }
  .quote-author { display: block; color: var(--lime-soft); font-style: normal; }

  /* front side */
  .card-front {
    top: 541px;
    background: linear-gradient(180deg, #ffffff 0%, #f4f4f4 100%);
  }
  .brand-name {
    position: absolute;
    top: 34px;
    left: 0;
    width: 100%;
    text-align: center;
    color: var(--plum-text);
    font-weight: 600;
    font-size: 24px;
    line-height: 1.15;
    letter-spacing: 0.5px;
  }
  .holder {
    position: absolute;
    top: 140px;
    right: 285px;
    text-align: right;
  }
  .holder-name {
    color: var(--plum-text);
    font-weight: 700;
    font-size: 21px;
    line-height: 1.2;
  }
  .holder-title {
    color: var(--ink);
    font-size: 17px;
    line-height: 1.2;
  }
  .divider {
    position: absolute;
    left: 270px;
    top: 142px;
    width: 1px;
    height: 68px;
    background: var(--divider);
  }
  .contacts {
    position: absolute;
    left: 284px;
    top: 144px;
    margin: 0;
    padding: 0;
    list-style: none;
    color: var(--ink);
    font-size: 15px;
    line-height: 22px;
  }
  .contacts li { display: flex; align-items: center; gap: 7px; white-space: nowrap; }
  .contacts svg { width: 13px; height: 13px; flex: none; }
  .swoosh {
    position: absolute;
    left: 0;
    top: 0;
    width: 540px;
    height: 309px;
  }
  .address {
    position: absolute;
    left: 52px;
    top: 264px;
    color: var(--ink);
    font-size: 15px;
    line-height: 18px;
    white-space: nowrap;
  }
</style>
</head>
<body>
<main class="stage">
  <section class="card card-back" aria-label="Card back">
    <p class="quote">
      <span class="quote-intro">The Dr. likes,</span>
      <span class="quote-body">“The doctor of the future will give no medicine, but will interest his patient in the care of the human frame, in diet and in the cause and prevention of disease.”</span>
      <span class="quote-author">- Walter Pimsley</span>
    </p>
  </section>

  <section class="card card-front" aria-label="Card front">
    <div class="brand-name">Valtesh<br>Spinal Care &amp; Performance</div>

    <svg class="swoosh" viewBox="0 0 540 309" aria-hidden="true">
      <path d="M40 222 C250 222 380 228 525 300 C378 232 250 226 40 225 Z" fill="var(--lime)"/>
    </svg>

    <div class="holder">
      <div class="holder-name">Dr. Marcus T. Valtesh</div>
      <div class="holder-title">President</div>
    </div>
    <div class="divider"></div>

    <ul class="contacts">
      <li>
        <svg viewBox="0 0 24 24"><path fill="var(--lime)" d="M6.6 10.8a15 15 0 0 0 6.6 6.6l2.2-2.2a1 1 0 0 1 1-.25 11.4 11.4 0 0 0 3.6.57 1 1 0 0 1 1 1V20a1 1 0 0 1-1 1A17 17 0 0 1 3 4a1 1 0 0 1 1-1h3.5a1 1 0 0 1 1 1c0 1.25.2 2.450.57 3.57a1 1 0 0 1-.25 1z"/></svg>
        (555) 014-2286
      </li>
      <li>
        <svg viewBox="0 0 24 24"><rect x="2" y="5" width="20" height="14" fill="none" stroke="var(--lime)" stroke-width="2"/><path d="M2 5l10 8 10-8" fill="none" stroke="var(--lime)" stroke-width="2"/></svg>
        marcus.v@valteshspinalcare.com
      </li>
      <li>
        <svg viewBox="0 0 24 24"><circle cx="12" cy="12" r="10" fill="none" stroke="var(--lime)" stroke-width="2"/><ellipse cx="12" cy="12" rx="4" ry="10" fill="none" stroke="var(--lime)" stroke-width="2"/><path d="M2 12h20" stroke="var(--lime)" stroke-width="2"/></svg>
        www.valteshspinalcare.com
      </li>
    </ul>

    <div class="address">418 N Alder Crest Rd, Suite B, Fairhaven, Illinois 60999</div>
  </section>
</main>
</body>
</html>
```